Maple Hollow Bloom Panels Business card

Looking to have a business card design incorporating my logo for my flower wall business.

Industry/Entity Type

Wedding & event planning

Contact Information for Business Card

My business logo, my name - Lena Whitcombe (owner), my tagline - Let us be your something extra, phone # 401-726-3148, email address - maplehollowbloompanels@mailvane.net, my website - maplehollowbloompanels.net, Instagram handle- @maplehollowbloompanels, FB handle Handle - maplehollowbloompanels

Font styles to use
Other font styles liked:
• Sentaina is the font that is used in my logo

Requirements
Must have
• Would like a double sided business card

```html
<!DOCTYPE html>
<html lang="en">
<head>
<meta charset="utf-8">
<title>Maple Hollow Bloom Panels – Business Card</title>
<link rel="stylesheet" href="https://fonts.googleapis.com/css2?family=Allura&family=Lato:wght@400;700&family=Cormorant+Garamond:wght@500&display=swap">
<style>
  :root {
    --page-bg: #e4e4e4;
    --card-bg: #fdfcfc;
    --ink: #1f1f1f;
    --blush: #f2a7bd;
    --blush-soft: rgba(242, 167, 189, 0.55);
    --peach-soft: rgba(246, 190, 185, 0.5);
    --card-shadow: 0 6px 18px rgba(0, 0, 0, 0.12);
  }
  * { margin: 0; padding: 0; box-sizing: border-box; }
  html, body { width: 1200px; height: 800px; overflow: hidden; background: var(--page-bg); }
  .canvas { position: relative; width: 1200px; height: 800px; }

  .card {
    position: absolute;
    width: 540px; height: 310px;
    background: var(--card-bg);
    box-shadow: var(--card-shadow);
    overflow: hidden;
    color: var(--ink);
  }
  .card--front { left: 40px; top: 245px; }
  .card--back { left: 620px; top: 245px; }

  .wash { position: absolute; border-radius: 50%; filter: blur(14px); }
  .wash--front-top { right: -70px; top: -60px; width: 200px; height: 230px;
    background: radial-gradient(circle at 45% 50%, var(--blush-soft), rgba(242,167,189,0) 70%); }
  .wash--front-left { left: -60px; top: 120px; width: 210px; height: 220px;
    background: radial-gradient(circle at 45% 50%, var(--blush), rgba(242,167,189,0) 70%); opacity: 0.75; }
  .wash--back-top { left: -40px; top: -70px; width: 260px; height: 200px;
    background: radial-gradient(circle at 55% 50%, var(--blush), rgba(242,167,189,0) 70%); opacity: 0.7; }
  .wash--back-bottom { right: -50px; bottom: -70px; width: 240px; height: 250px;
    background: radial-gradient(circle at 45% 45%, var(--peach-soft), rgba(242,167,189,0.4) 45%, rgba(242,167,189,0) 72%); }

  .tagline {
    position: absolute; top: 20px; left: 0; right: 0; text-align: center;
    font-family: "Lato", sans-serif; font-weight: 700; font-size: 11px;
    letter-spacing: 3px;
  }
  .wordmark {
    position: absolute; top: 118px; left: 0; right: 0; text-align: center;
    font-family: "Allura", cursive; font-size: 52px; line-height: 1;
  }

  .badge {
    position: absolute; top: 20px; left: 0; right: 0;
    display: flex; flex-direction: column; align-items: center; gap: 4px;
  }
  .badge__circle { width: 34px; height: 34px; border-radius: 50%; border: 1px solid #d7c38f; }
  .badge__name { font-family: "Allura", cursive; font-size: 16px; line-height: 1; }

  .owner-name {
    position: absolute; top: 92px; left: 0; right: 0; text-align: center;
    font-family: "Allura", cursive; font-size: 44px; line-height: 1;
  }
  .owner-title {
    position: absolute; top: 142px; left: 0; right: 0; text-align: center;
    font-family: "Cormorant Garamond", serif; font-size: 12px; letter-spacing: 6px;
  }

  .contact-frame {
    position: absolute; left: 18px; right: 18px; top: 172px; bottom: 14px;
    border: 1.5px solid var(--ink); border-radius: 12px;
  }
  .social { position: absolute; left: 16px; top: 14px; font-family: "Lato", sans-serif; font-size: 12px; }
  .social__row { display: flex; align-items: center; gap: 7px; line-height: 19px; }
  .social__dot { width: 10px; height: 10px; border-radius: 50%; background: var(--ink); flex: none; }
  .details {
    position: absolute; right: 16px; bottom: 12px; text-align: right;
    font-family: "Lato", sans-serif; font-size: 12px; line-height: 18px;
  }
</style>
</head>
<body>
<main class="canvas">

  <section class="card card--front" aria-label="Card front">
    <div class="wash wash--front-top" role="img" aria-label="Soft pink watercolour wash"></div>
    <div class="wash wash--front-left" role="img" aria-label="Soft pink watercolour wash"></div>
    <p class="tagline">Let us be your something extra</p>
    <h1 class="wordmark">Maple Hollow Bloom Panels</h1>
  </section>

  <section class="card card--back" aria-label="Card back">
    <div class="wash wash--back-top" role="img" aria-label="Soft pink watercolour wash"></div>
    <div class="wash wash--back-bottom" role="img" aria-label="Soft pink and peach watercolour wash"></div>

    <div class="badge">
      <span class="badge__circle"></span>
      <span class="badge__name">Maple Hollow Bloom Panels</span>
    </div>

    <h2 class="owner-name">Lena Whitcombe</h2>
    <p class="owner-title">• owner •</p>

    <div class="contact-frame">
      <div class="social">
        <p class="social__row"><span class="social__dot"></span>Handle - maplehollowbloompanels</p>
        <p class="social__row"><span class="social__dot"></span>@maplehollowbloompanels</p>
      </div>
      <div class="details">
        <p>maplehollowbloompanels.net</p>
        <p>401-726-3148</p>
        <p>maplehollowbloompanels@mailvane.net</p>
        <p>maplehollowbloompanels.net</p>
      </div>
    </div>
  </section>

</main>
</body>
</html>
```